TalkBridge - Language Coaching Services

Sleek, innovative, trendy design for Language Coaching business.

TalkBridge is a new UK based company that provides Language Coaching services. We offer highly personalized on-line and face to face language courses. We also impart learning techniques workshops based on the latest neuroscience research for second-language acquisition.

Target Market(s)

Industry/Entity Type

Consulting

Contact Information for Business Card

TalkBridge
ElenaVT@talkbridge-demo.co.uk
TalkBridge-demo.co.uk
London, UK

Font styles to use
Sans Serif

```html
<!DOCTYPE html>
<html lang="en">
<head>
<meta charset="utf-8">
<title>TalkBridge – Business Card</title>
<link rel="stylesheet" href="https://fonts.googleapis.com/css2?family=Open+Sans:wght@400;600;700&display=swap">
<style>
  :root {
    --page: #e9ebed;
    --card: #f7f8f9;
    --card-edge: #d4d8dc;
    --brand-blue: #175a80;
    --brand-blue-soft: #4d83a3;
    --ink: #3a4148;
  }
  html, body {
    margin: 0;
    padding: 0;
    width: 1200px;
    height: 970px;
    overflow: hidden;
    background: var(--page);
    font-family: "Open Sans", sans-serif;
  }
  .card {
    position: absolute;
    left: 85px;
    top: 198px;
    width: 1030px;
    height: 575px;
    box-sizing: border-box;
    background: var(--card);
    border: 2px solid var(--card-edge);
    border-radius: 34px 120px 120px 34px;
    box-shadow: 0 10px 30px rgba(0, 0, 0, 0.08);
  }
  .wordmark {
    position: absolute;
    left: 44px;
    top: 70px;
    margin: 0;
    font-size: 64px;
    font-weight: 600;
    letter-spacing: 2px;
    color: var(--brand-blue);
    line-height: 1;
  }
  .person {
    position: absolute;
    left: 49px;
    top: 236px;
  }
  .person-name {
    margin: 0;
    font-size: 27px;
    font-weight: 700;
    color: var(--brand-blue);
    letter-spacing: 0.5px;
    line-height: 1.2;
  }
  .person-title {
    margin: 2px 0 0;
    font-size: 23px;
    color: var(--ink);
  }
  .address {
    position: absolute;
    left: 49px;
    top: 336px;
    margin: 0;
    font-style: normal;
    font-size: 23px;
    line-height: 1.4;
    color: var(--ink);
  }
  .contact-list {
    position: absolute;
    left: 49px;
    top: 418px;
    margin: 0;
    padding: 0;
    list-style: none;
    font-size: 23px;
    line-height: 31px;
    color: var(--ink);
  }
  .contact-list li {
    display: flex;
    align-items: center;
    gap: 8px;
  }
  .contact-icon {
    width: 18px;
    height: 18px;
    fill: var(--ink);
    flex: none;
  }
  .brand-symbol-area {
    position: absolute;
    left: 473px;
    top: 33px;
    width: 508px;
    height: 508px;
    border-radius: 50%;
    background: radial-gradient(circle at 50% 45%, var(--brand-blue-soft) 0%, var(--brand-blue) 100%);
    opacity: 0.18;
  }
</style>
</head>
<body>
  <section class="card">
    <h1 class="wordmark">TALKBRIDGE</h1>

    <div class="person">
      <p class="person-name">ELENA VARELA</p>
      <p class="person-title">Chief Managing Officer</p>
    </div>

    <address class="address">14 Harrow Lane, Suite 3<br>London UK W1A 4BX</address>

    <ul class="contact-list">
      <li>
        <svg class="contact-icon" viewBox="0 0 18 18" aria-hidden="true"><path d="M2 5c0-2 3-3 7-3s7 1 7 3v1h-4V5H6v1H2z M4 8h10l2 7H2z"/></svg>
        + 000 000 0000
      </li>
      <li>
        <svg class="contact-icon" viewBox="0 0 18 18" aria-hidden="true"><path d="M5 2h8v4H5z M2 7h14v6h-3v3H5v-3H2z M6 11v3h6v-3z"/></svg>
        + 000 000 0000
      </li>
      <li>
        <svg class="contact-icon" viewBox="0 0 18 18" aria-hidden="true"><path d="M1 4h16v10H1z" fill="none" stroke="#3a4148" stroke-width="1.6"/><path d="M1 4l8 6 8-6" fill="none" stroke="#3a4148" stroke-width="1.6"/></svg>
        ElenaVT@talkbridge-demo.co.uk
      </li>
      <li>
        <svg class="contact-icon" viewBox="0 0 18 18" aria-hidden="true"><circle cx="9" cy="9" r="7.5" fill="none" stroke="#3a4148" stroke-width="1.6"/><path d="M1.5 9h15 M9 1.5c-3 3-3 12 0 15 M9 1.5c3 3 3 12 0 15" fill="none" stroke="#3a4148" stroke-width="1.3"/></svg>
        www.talkbridge-demo.co.uk
      </li>
    </ul>

    <div class="brand-symbol-area" role="img" aria-label="Space for the TalkBridge brand symbol"></div>
  </section>
</body>
</html>
```